Corporate identity and pre-opening design for a brand new Casino

Dear designers!

We need a design for the pre-opening ad campaign of our brand new casino called "Velmora Casino" and planned to open soon.
It is situated in "Ostrel Lodge Ruzhan" – a 4-star luxury and business hotel, located in the city of Plovdiv, Bulgaria.
Our vision of the project is bold, but stylish and elegant. We desire to see uniqueness by all means.
Our slogan is “So many ways to have fun”.
We need a design for our ad campaign for ex. billbord 8m x 4m. We expect your elegant and creative designs. We are trying to avoid the conventional, but at the same time we do not want to be too extravagant.

Thank you and good luck!

Requirements
Should not have
• dices

```html
<!DOCTYPE html>
<html lang="en">
<head>
<meta charset="utf-8">
<title>Velmora Casino — Opening Soon Billboard</title>
<link rel="stylesheet" href="https://fonts.googleapis.com/css2?family=Arimo:wght@700&family=Marcellus&display=swap">
<style>
  :root {
    --page-bg: #e6e6e6;
    --orange: #f6961f;
    --white: #ffffff;
    --ink: #0b0b0b;
    --divider: #2a2a2a;
    --accent-red: #e63a24;
    --accent-orange: #f26a21;
  }
  * { margin: 0; padding: 0; box-sizing: border-box; }
  html, body {
    width: 1200px;
    height: 704px;
    overflow: hidden;
    background: var(--page-bg);
  }
  .billboard {
    position: absolute;
    left: 20px;
    top: 62px;
    width: 1160px;
    height: 580px;
    display: flex;
    box-shadow: 0 10px 24px rgba(0,0,0,0.25);
  }
  .panel {
    position: relative;
    width: 580px;
    height: 580px;
    overflow: hidden;
  }
  .panel--orange { background: var(--orange); }
  .panel--white {
    background: var(--white);
    border-left: 4px solid var(--divider);
  }
  .brand-name {
    position: absolute;
    left: 0;
    right: 0;
    top: 150px;
    text-align: center;
    font-family: "Marcellus", serif;
    font-size: 44px;
    letter-spacing: 2px;
    line-height: 1;
  }
  .panel--orange .brand-name { color: var(--white); }
  .panel--white .brand-name { color: var(--ink); }
  .headline {
    position: absolute;
    left: 0;
    right: 0;
    top: 266px;
    text-align: center;
    font-family: "Arimo", sans-serif;
    font-weight: 700;
    color: var(--ink);
    line-height: 1;
  }
  .headline__top {
    display: block;
    font-size: 66px;
    letter-spacing: 1px;
  }
  .headline__bottom {
    display: block;
    font-size: 112px;
    margin-top: -4px;
  }
  .accent-pattern {
    position: absolute;
    right: 0;
    top: 173px;
    width: 146px;
    height: 407px;
  }
  .slogan {
    position: absolute;
    left: 0;
    width: 1160px;
    top: 512px;
    text-align: center;
    font-family: "Marcellus", serif;
    font-size: 42px;
    font-weight: 400;
    color: var(--ink);
    letter-spacing: 1px;
    -webkit-text-stroke: 0.8px var(--ink);
    white-space: nowrap;
    transform: translateX(-20px);
  }
</style>
</head>
<body>
  <main class="billboard">
    <section class="panel panel--orange">
      <p class="brand-name">VELMORA CASINO</p>
      <h1 class="headline">
        <span class="headline__top">OPENING</span>
        <span class="headline__bottom">SOON</span>
      </h1>
    </section>
    <section class="panel panel--white">
      <p class="brand-name">VELMORA CASINO</p>
      <h2 class="headline">
        <span class="headline__top">OPENING</span>
        <span class="headline__bottom">SOON</span>
      </h2>
      <svg class="accent-pattern" viewBox="0 0 146 407" role="img" aria-label="Decorative cascade of orange and red diamond shapes along the right edge">
        <defs>
          <linearGradient id="accentFill" x1="0" y1="0" x2="0" y2="1">
            <stop offset="0" stop-color="var(--accent-orange)" />
            <stop offset="0.5" stop-color="var(--accent-red)" />
            <stop offset="1" stop-color="var(--accent-orange)" />
          </linearGradient>
        </defs>
        <polygon points="146,0 146,407 0,407 30,330 60,240 80,150 110,60" fill="url(#accentFill)" opacity="0.9" />
      </svg>
    </section>
    <p class="slogan">SO MANY WAYS TO HAVE FUN</p>
  </main>
</body>
</html>
```